Zielgruppe
Wir machen Softwareentwicklung. Die Zielgruppe sind Geschäftsführer und Leute aus Leitungspositionen aus dem IT Bereich.
Aufgabenstellung
Ich fände es toll, zwei Designs zu haben. Eine etwas seriösere für Geschäftstermine und eine lockere/verspielte für Meetups und Termine an denen ich eher Angestellte suche.
Bitte auch eine Variante mit QR Code.
Die Angaben auf der Visitenkarte sind:
Max Mustermann (Name des Angestellten)
Position
Adresse-Strasse
Adresse-Postleitzahl und Ort
Telefonnummer (bitte keine Fax-Nummer)
Emailadresse
Webadresse

```html
<!DOCTYPE html>
<html lang="de">
<head>
<meta charset="utf-8">
<title>Codewerk Falkner – Visitenkarte</title>
<link rel="stylesheet" href="https://fonts.googleapis.com/css2?family=Noto+Sans:wght@400;700&display=swap">
<style>
  :root {
    --backdrop: #d9d7d4;
    --card-dark: #343c44;
    --card-light: #f0f0f0;
    --brand-blue: #1a8fd6;
    --ink: #343c44;
    --ink-soft: #3f464d;
    --icon-fg: #ffffff;
  }
  * { margin: 0; padding: 0; box-sizing: border-box; }
  html, body {
    width: 1200px; height: 1200px; overflow: hidden;
    background: var(--backdrop);
    font-family: "Noto Sans", sans-serif;
  }
  .canvas { position: relative; width: 1200px; height: 1200px; }

  .card {
    position: absolute; left: 210px; width: 780px; height: 444px;
    box-shadow: 0 6px 18px rgba(0,0,0,0.18);
  }
  .card--front { top: 140px; background: var(--card-dark); }
  .card--back  { top: 649px; background: var(--card-light); }

  .brand {
    position: absolute; display: flex; align-items: center;
  }
  .brand__square {
    border: 3px solid var(--brand-blue); border-radius: 10px; flex: none;
  }
  .brand__name {
    color: var(--brand-blue); font-weight: 700; line-height: 1.05;
    text-transform: uppercase; letter-spacing: 0.5px;
  }
  .card--front .brand { left: 215px; top: 170px; gap: 22px; }
  .card--front .brand__square { width: 96px; height: 96px; }
  .card--front .brand__name { font-size: 38px; }

  .card--back .brand { left: 87px; top: 209px; gap: 12px; }
  .card--back .brand__square { width: 52px; height: 52px; border-width: 2px; border-radius: 6px; }
  .card--back .brand__name { font-size: 20px; }

  .divider {
    position: absolute; left: 386px; top: 90px; width: 4px; height: 290px;
    background: linear-gradient(to bottom, rgba(0,0,0,0), rgba(0,0,0,0.10), rgba(0,0,0,0));
    filter: blur(1.5px);
  }

  .person { position: absolute; left: 502px; top: 76px; color: var(--ink); }
  .person__name { font-size: 21px; letter-spacing: 0.6px; }
  .person__name strong { font-weight: 700; }
  .person__role { font-size: 13.5px; margin-top: 1px; color: var(--ink-soft); }

  .contact { position: absolute; left: 445px; top: 158px; list-style: none; }
  .contact__item {
    position: absolute; left: 0; display: flex; align-items: center; gap: 19px;
    color: var(--ink-soft); font-size: 16px; letter-spacing: 0.3px; white-space: nowrap;
  }
  .contact__item:nth-child(1) { top: 0; }
  .contact__item:nth-child(2) { top: 58px; }
  .contact__item:nth-child(3) { top: 121px; }
  .contact__item:nth-child(4) { top: 178px; }
  .contact__icon {
    width: 38px; height: 38px; border-radius: 50%; background: var(--ink);
    display: flex; align-items: center; justify-content: center; flex: none;
  }
  .contact__text { line-height: 1.25; }
</style>
</head>
<body>
<main class="canvas">

  <section class="card card--front" aria-label="Vorderseite">
    <div class="brand">
      <span class="brand__square"></span>
      <span class="brand__name">Codewerk<br>Falkner</span>
    </div>
  </section>

  <section class="card card--back" aria-label="Rückseite">
    <div class="brand">
      <span class="brand__square"></span>
      <span class="brand__name">Codewerk<br>Falkner</span>
    </div>

    <div class="divider"></div>

    <div class="person">
      <p class="person__name">MAX <strong>MUSTERMAN</strong></p>
      <p class="person__role">Leiter Entwicklung</p>
    </div>

    <ul class="contact">
      <li class="contact__item">
        <span class="contact__icon">
          <svg width="20" height="18" viewBox="0 0 20 18"><path d="M10 1 L19 9 H16 V17 H12 V12 H8 V17 H4 V9 H1 Z" fill="var(--icon-fg)"/></svg>
        </span>
        <span class="contact__text">Adresse-Strasse<br>Adresse-Postleitzahl</span>
      </li>
      <li class="contact__item">
        <span class="contact__icon">
          <svg width="18" height="18" viewBox="0 0 24 24"><path d="M6.6 10.8a15.1 15.1 0 0 0 6.6 6.6l2.2-2.2c.3-.3.7-.4 1-.2 1.1.4 2.3.6 3.6.6.6 0 1 .4 1 1V20c0 .6-.4 1-1 1C10.6 21 3 13.4 3 4c0-.6.4-1 1-1h3.5c.6 0 1 .4 1 1 0 1.3.2 2.5.6 3.6.1.3 0 .7-.2 1z" fill="var(--icon-fg)"/></svg>
        </span>
        <span class="contact__text">+43 1 512 77 40</span>
      </li>
      <li class="contact__item">
        <span class="contact__icon">
          <svg width="20" height="14" viewBox="0 0 20 14"><rect x="0.5" y="0.5" width="19" height="13" fill="var(--icon-fg)"/><path d="M1 1 L10 8 L19 1 M1 13 L7.5 6.5 M19 13 L12.5 6.5" stroke="var(--ink)" stroke-width="1.3" fill="none"/></svg>
        </span>
        <span class="contact__text">office@codewerk-falkner.at</span>
      </li>
      <li class="contact__item">
        <span class="contact__icon">
          <svg width="20" height="20" viewBox="0 0 20 20"><circle cx="10" cy="10" r="8.5" fill="none" stroke="var(--icon-fg)" stroke-width="1.8"/><ellipse cx="10" cy="10" rx="3.6" ry="8.5" fill="none" stroke="var(--icon-fg)" stroke-width="1.4"/><path d="M1.5 10 H18.5" stroke="var(--icon-fg)" stroke-width="1.4"/></svg>
        </span>
        <span class="contact__text">www.codewerk-falkner.at</span>
      </li>
    </ul>
  </section>

</main>
</body>
</html>
```